New Zealand Marlborough Sauvignon Blanc wine packaging design

We need packaging design for our new wine brand, Dunmore Hale. The wine is a New Zealand Marlborough Sauvignon Blanc. We would like the packaging will portray elegance and style with an understated label. We are looking for a label that portrays the elegance of the French Riviera. The label should be round or pill shaped.
Updates

Industry/Entity Type

Wine

Font styles to use
Serif
Sans Serif

Requirements
Must have
• The words in order of importance: Dunmore Hale, Sauvignon Blanc, Marlborough, New Zealand. It should be fit to the bottle posted in the links
Nice to have
• a pill shape or circular shape
Should not have
• Illustrations of wine bottles, wine glasses, or grapes

```html
<!DOCTYPE html>
<html lang="en">
<head>
<meta charset="utf-8">
<title>Dunmore Hale — Sauvignon Blanc Label</title>
<link rel="stylesheet" href="https://fonts.googleapis.com/css2?family=Rye&family=Barlow:wght@500;600&display=swap">
<style>
  :root {
    --backdrop: #353535;
    --label-ink: #231f20;
    --gold: #c9a34a;
    --gold-muted: #6e5a2c;
    --cream: #f1ead8;
  }
  html, body {
    margin: 0;
    padding: 0;
    width: 1200px;
    height: 1184px;
    overflow: hidden;
    background: var(--backdrop);
  }
  .canvas {
    width: 1200px;
    height: 1184px;
    display: block;
  }
  .brand-arch {
    font-family: "Rye", serif;
    font-size: 78px;
    fill: var(--gold);
    letter-spacing: 2px;
  }
  .varietal {
    font-family: "Barlow", sans-serif;
    font-weight: 600;
    font-size: 36px;
    fill: var(--cream);
    letter-spacing: 5px;
  }
  .region {
    font-family: "Barlow", sans-serif;
    font-weight: 500;
    font-size: 28px;
    fill: var(--gold);
    letter-spacing: 6px;
  }
  .est-mark {
    font-family: "Barlow", sans-serif;
    font-weight: 500;
    font-size: 28px;
    fill: var(--gold);
    letter-spacing: 3px;
  }
  .centre-name {
    font-family: "Barlow", sans-serif;
    font-weight: 600;
    font-size: 32px;
    fill: var(--gold);
    letter-spacing: 4px;
  }
</style>
</head>
<body>
<svg class="canvas" viewBox="0 0 1200 1184" xmlns="http://www.w3.org/2000/svg">
  <defs>
    <path id="arch-top" d="M 322 640 A 280 280 0 1 1 878 640"/>
    <path id="arch-varietal" d="M 340 592 A 260 260 0 0 0 860 592"/>
    <path id="arch-region" d="M 212 592 A 388 388 0 0 0 988 592"/>
  </defs>

  <g class="label">
    <!-- outer disc -->
    <circle cx="600" cy="592" r="440" fill="var(--label-ink)"/>
    <circle cx="600" cy="592" r="420" fill="none" stroke="var(--gold)" stroke-width="3"/>

    <!-- edge diamonds -->
    <g class="edge-diamonds" fill="var(--gold)">
      <path d="M600 146 l10 14 l-10 14 l-10 -14 z"/>
      <path d="M600 1010 l10 14 l-10 14 l-10 -14 z"/>
      <path d="M156 592 l14 -10 l14 10 l-14 10 z"/>
      <path d="M1016 592 l14 -10 l14 10 l-14 10 z"/>
    </g>

    <!-- radiating band -->
    <path class="ray-band" role="img" aria-label="Fine radiating gold rays around the upper rim"
          d="M 224 652 A 381 381 0 1 1 976 652" fill="none" stroke="var(--gold-muted)" stroke-width="40"/>
    <circle cx="600" cy="592" r="358" fill="none" stroke="var(--gold)" stroke-width="2.5"/>
    <circle cx="600" cy="592" r="404" fill="none" stroke="var(--gold)" stroke-width="1.5"/>

    <!-- arched brand name -->
    <text class="brand-arch"><textPath href="#arch-top" startOffset="50%" text-anchor="middle">DUNMORE HALE</textPath></text>

    <!-- horizontal band -->
    <g class="est-band">
      <rect x="248" y="652" width="704" height="62" fill="var(--label-ink)"/>
      <line x1="248" y1="652" x2="952" y2="652" stroke="var(--gold)" stroke-width="2.5"/>
      <line x1="248" y1="714" x2="952" y2="714" stroke="var(--gold)" stroke-width="2.5"/>
      <text class="est-mark" x="318" y="694" text-anchor="middle">EST.</text>
      <text class="est-mark" x="882" y="694" text-anchor="middle">2018</text>
    </g>

    <!-- centre medallion -->
    <g class="medallion">
      <circle cx="600" cy="592" r="218" fill="var(--label-ink)" stroke="var(--gold)" stroke-width="2.5"/>
      <circle cx="600" cy="592" r="200" fill="none" stroke="var(--gold-muted)" stroke-width="14"
              role="img" aria-label="Fine tick ring inside the medallion"/>
      <circle cx="600" cy="592" r="188" fill="none" stroke="var(--gold)" stroke-width="2"/>
      <g class="medallion-bars" stroke="var(--gold)" stroke-width="3">
        <line x1="592" y1="364" x2="592" y2="386"/>
        <line x1="600" y1="364" x2="600" y2="386"/>
        <line x1="608" y1="364" x2="608" y2="386"/>
        <line x1="592" y1="798" x2="592" y2="820"/>
        <line x1="600" y1="798" x2="600" y2="820"/>
        <line x1="608" y1="798" x2="608" y2="820"/>
      </g>
      <text class="centre-name" x="600" y="603" text-anchor="middle">DUNMORE HALE</text>
    </g>

    <!-- lower texts -->
    <text class="varietal"><textPath href="#arch-varietal" startOffset="50%" text-anchor="middle">SAUVIGNON BLANC</textPath></text>
    <text class="region"><textPath href="#arch-region" startOffset="50%" text-anchor="middle">MARLBOROUGH, NUEVA ZELANDA</textPath></text>
  </g>
</svg>
</body>
</html>
```